Creative Design "Size Chart" for a Clothing Product

Hi, My dear friends! I am looking to do a contest to design a unique creative "Size Chart" for our clothing line. See Attached the Sizes & Ideas Thanks Good Luck Osvald

Colors

Designer to choose colors to be used in the design.

```html
<!DOCTYPE html>
<html lang="en">
<head>
<meta charset="utf-8">
<title>Size Chart</title>
<link rel="stylesheet" href="https://fonts.googleapis.com/css2?family=Archivo+Black&family=Archivo:wght@700;800&display=swap">
<style>
  :root {
    --ink: #000000;
    --paper: #ffffff;
    --panel: #e5e5e5;
    --chest: #0000ff;
    --waist: #ff0000;
    --garment: #ffffff;
  }
  * { box-sizing: border-box; margin: 0; padding: 0; }
  html, body { width: 936px; height: 1200px; overflow: hidden; background: var(--paper); }
  .canvas {
    position: relative;
    width: 936px;
    height: 1200px;
    border: 1.5px solid var(--ink);
    background: var(--paper);
  }
  .panel {
    position: absolute;
    left: 83px;
    width: 769px;
    height: 486px;
    background: var(--panel);
    border: 2px solid var(--ink);
    border-radius: 44px;
  }
  .panel--mens { top: 75px; }
  .panel--womens { top: 624px; }
  .panel-title {
    position: absolute;
    font-family: "Archivo Black", "Arial Black", sans-serif;
    font-size: 41px;
    line-height: 1;
    color: var(--ink);
    letter-spacing: 1px;
    transform: translateX(-50%);
    white-space: nowrap;
  }
  .panel--mens .panel-title { left: 191px; top: 42px; }
  .panel--womens .panel-title { left: 164px; top: 49px; }
  .garment {
    position: absolute;
    background: var(--garment);
    border: 1.5px solid var(--ink);
    border-radius: 14px;
  }
  .panel--mens .garment { left: 30px; top: 92px; width: 324px; height: 346px; }
  .panel--womens .garment { left: 16px; top: 104px; width: 296px; height: 317px; }
  .size-table {
    position: absolute;
    list-style: none;
  }
  .panel--mens .size-table { left: 403px; top: 44px; }
  .panel--womens .size-table { left: 315px; top: 9px; }
  .size-row {
    display: flex;
    align-items: center;
    gap: 8px;
    height: 55px;
    margin-bottom: 13.2px;
    padding: 0 5px;
    border: 2px solid var(--ink);
    border-radius: 28px;
    background: var(--panel);
    font-family: "Archivo", Arial, sans-serif;
    font-weight: 800;
    color: var(--paper);
  }
  .panel--mens .size-row { width: 335px; font-size: 24px; }
  .panel--womens .size-row { width: 440px; font-size: 22px; }
  .size-label, .chest, .waist {
    display: flex;
    align-items: center;
    justify-content: center;
    height: 43px;
    border-radius: 22px;
    white-space: nowrap;
  }
  .size-label { background: var(--ink); }
  .panel--mens .size-label { width: 43px; border-radius: 50%; font-size: 21px; letter-spacing: -0.5px; }
  .panel--womens .size-label { width: 148px; }
  .chest { background: var(--chest); width: 130px; }
  .waist { background: var(--waist); width: 132px; }
</style>
</head>
<body>
<main class="canvas">
  <section class="panel panel--mens">
    <h2 class="panel-title">MENS</h2>
    <div class="garment" role="img" aria-label="Men's shirt outline with blue chest (C) and red waist (W) measurement lines"></div>
    <ul class="size-table">
      <li class="size-row"><span class="size-label">S</span><span class="chest">34-36</span><span class="waist">28-30</span></li>
      <li class="size-row"><span class="size-label">M</span><span class="chest">36-38</span><span class="waist">30-32</span></li>
      <li class="size-row"><span class="size-label">L</span><span class="chest">38-40</span><span class="waist">32-34</span></li>
      <li class="size-row"><span class="size-label">XL</span><span class="chest">40-42</span><span class="waist">34-36</span></li>
      <li class="size-row"><span class="size-label">2X</span><span class="chest">43-45</span><span class="waist">36-40</span></li>
      <li class="size-row"><span class="size-label">3X</span><span class="chest">45-48</span><span class="waist">40-44</span></li>
    </ul>
  </section>

  <section class="panel panel--womens">
    <h2 class="panel-title">WOMENS</h2>
    <div class="garment" role="img" aria-label="Women's fitted shirt outline with blue chest (C) and red waist (W) measurement lines"></div>
    <ul class="size-table">
      <li class="size-row"><span class="size-label">XS (0-2)</span><span class="chest">32-34</span><span class="waist">26-28</span></li>
      <li class="size-row"><span class="size-label">S (4-6)</span><span class="chest">34-36</span><span class="waist">28-30</span></li>
      <li class="size-row"><span class="size-label">M (8-10)</span><span class="chest">36-38</span><span class="waist">30-32</span></li>
      <li class="size-row"><span class="size-label">L (12-14)</span><span class="chest">38-40</span><span class="waist">32-34</span></li>
      <li class="size-row"><span class="size-label">XL (14-16 )</span><span class="chest">40-42</span><span class="waist">34-36</span></li>
      <li class="size-row"><span class="size-label">2X (18)</span><span class="chest">42-44</span><span class="waist">36-38</span></li>
      <li class="size-row"><span class="size-label">3X (20)</span><span class="chest">44-46</span><span class="waist">38-40</span></li>
    </ul>
  </section>
</main>
</body>
</html>
```